Bright Fern Custom Homes business card. Double sided. Modern. professional

Bright Fern Custom Homes
contemporary modern design with our logo /
Double sided with all our contact information
Use same Green colors as in our Logo. Contemporary logo that grabs your attention. Visually pleasing and balanced. Easy to read, and Vibrant. Would love an option for rounded edges. Embossed logo would be amazing.
Contact Information for Business Card
Dana Welk Owner / General Contractor Bright Fern Custom Homes p: 704.552.1830 m: 912.648.2071 e: brightferncustomhomes@mailbox.example w: www.brightferncustomhomes.example 218 Pryor Meadow Lane Alder Ridge, NV 29041

```html
<!DOCTYPE html>
<html lang="en">
<head>
<meta charset="utf-8">
<title>Bright Fern Custom Homes — Business Card</title>
<link href="https://fonts.googleapis.com/css2?family=Cinzel:wght@400;500&family=Arimo:wght@400&display=swap" rel="stylesheet">
<style>
  :root {
    --canvas: #d9d9d9;
    --card-dark: #222222;
    --card-light: #ffffff;
    --green: #6b8f2f;
    --green-deep: #55742a;
    --green-light: #7f9f3c;
    --ink: #2b2b2b;
    --ink-soft: #555555;
  }
  * { box-sizing: border-box; margin: 0; padding: 0; }
  html, body { width: 1200px; height: 900px; overflow: hidden; }
  body { background: var(--canvas); position: relative; font-family: "Arimo", Arial, sans-serif; }

  .card {
    position: absolute;
    width: 525px;
    height: 300px;
    border-radius: 18px;
    overflow: hidden;
    box-shadow: 0 14px 28px rgba(0,0,0,0.18);
  }

  /* Front side */
  .card--front {
    left: 80px; top: 150px;
    background: var(--card-dark);
    display: flex; align-items: center; justify-content: center;
  }
  .brand {
    display: flex; flex-direction: column; align-items: center; gap: 14px;
    color: var(--green);
    font-family: "Cinzel", Georgia, serif;
    font-weight: 400;
    text-align: center;
  }
  .brand__dot { width: 26px; height: 26px; border-radius: 50%; background: var(--green); }
  .brand__name { font-size: 34px; letter-spacing: 2px; line-height: 1.1; }
  .brand__sub { font-size: 13px; letter-spacing: 7px; line-height: 1; }

  /* Back side */
  .card--back {
    left: 595px; top: 450px;
    background: var(--card-light);
  }
  .back__decor {
    position: absolute;
    left: 0; bottom: 0;
    width: 225px; height: 190px;
    background: linear-gradient(160deg, var(--green-light) 0%, var(--green) 55%, var(--green-deep) 100%);
    border-top-right-radius: 120px 180px;
  }
  .contact {
    position: absolute;
    right: 26px; top: 24px;
    text-align: right;
    color: var(--ink);
    font-size: 12px;
    line-height: 1.45;
  }
  .contact__name {
    font-family: "Cinzel", Georgia, serif;
    color: var(--green);
    font-size: 25px;
    font-weight: 500;
    line-height: 1;
  }
  .contact__title { color: var(--ink-soft); font-size: 12px; margin-bottom: 10px; }
  .contact__address { margin-bottom: 8px; }
  .contact__line { display: flex; justify-content: flex-end; align-items: center; gap: 6px; white-space: nowrap; }
  .contact__line svg { width: 11px; height: 11px; fill: var(--green); flex: none; }
</style>
</head>
<body>

<section class="card card--front" aria-label="Card front">
  <div class="brand">
    <span class="brand__dot" aria-hidden="true"></span>
    <span class="brand__name">BRIGHT FERN</span>
    <span class="brand__sub">CUSTOM HOMES</span>
  </div>
</section>

<section class="card card--back" aria-label="Card back">
  <div class="back__decor" role="img" aria-label="Large green brand decoration"></div>
  <div class="contact">
    <p class="contact__name">DANA WELK</p>
    <p class="contact__title">Owner/General Contractor</p>
    <p class="contact__address">218 Pryor Meadow Lane<br>Alder Ridge, NV 29041</p>
    <p class="contact__line">704.552.1830
      <svg viewBox="0 0 24 24" aria-hidden="true"><path d="M6.6 10.8a15 15 0 0 0 6.6 6.6l2.2-2.2a1 1 0 0 1 1-.25 11.4 11.4 0 0 0 3.6.57 1 1 0 0 1 1 1V20a1 1 0 0 1-1 1A17 17 0 0 1 3 4a1 1 0 0 1 1-1h3.5a1 1 0 0 1 1 1c0 1.25.2 2.450.57 3.57a1 1 0 0 1-.25 1z"/></svg>
    </p>
    <p class="contact__line">912.648.2071
      <svg viewBox="0 0 24 24" aria-hidden="true"><path d="M7 1h10a2 2 0 0 1 2 2v18a2 2 0 0 1-2 2H7a2 2 0 0 1-2-2V3a2 2 0 0 1 2-2zm0 3v14h10V4zm5 15.5a1 1 0 1 0 0 2 1 1 0 0 0 0-2z"/></svg>
    </p>
    <p class="contact__line">brightferncustomhomes@mailbox.example
      <svg viewBox="0 0 24 24" aria-hidden="true"><path d="M2 5h20v14H2zm2 2v.5l8 5 8-5V7zm0 2.8V17h16V9.8l-8 5z"/></svg>
    </p>
    <p class="contact__line">brightferncustomhomes.example
      <svg viewBox="0 0 24 24" aria-hidden="true"><path d="M12 2a10 10 0 1 0 0 20 10 10 0 0 0 0-20zm6.9 9h-3a15 15 0 0 0-1.3-5.5A8 8 0 0 1 18.9 11zM12 4c.9 1.2 1.8 3.6 1.9 7h-3.8c.1-3.4 1-5.8 1.9-7zM9.4 5.5A15 15 0 0 0 8.1 11h-3a8 8 0 0 1 4.3-5.5zM5.1 13h3a15 15 0 0 0 1.3 5.5A8 8 0 0 1 5.1 13zm6.9 7c-.9-1.2-1.8-3.6-1.9-7h3.8c-.1 3.4-1 5.8-1.9 7zm2.6-1.5a15 15 0 0 0 1.3-5.5h3a8 8 0 0 1-4.3 5.5z"/></svg>
    </p>
  </div>
</section>

</body>
</html>
```